Business Consulting Business Card

professional business card with basic information (1) First and Last name (2) email address, (3) phone number, (4) website.

```html
<!DOCTYPE html>
<html lang="en">
<head>
<meta charset="utf-8">
<title>Tidemere – Business Card</title>
<link rel="stylesheet" href="https://fonts.googleapis.com/css2?family=Montserrat:wght@500;600&family=Arimo:wght@400&display=swap">
<style>
  :root {
    --backdrop: #2f2f2f;
    --paper: #ffffff;
    --teal: #4fbab3;
    --ocean: #4aa1c2;
    --navy: #163244;
    --ink: #2a2a2a;
    --rule: #cfcfcf;
    --ghost: rgba(0, 0, 0, 0.045);
  }
  * { box-sizing: border-box; margin: 0; padding: 0; }
  html, body { width: 1200px; height: 866px; overflow: hidden; }
  body {
    background: var(--backdrop);
    position: relative;
  }
  .card {
    position: absolute;
    left: 260px;
    width: 680px;
    height: 389px;
    overflow: hidden;
    box-shadow: 0 6px 18px rgba(0, 0, 0, 0.45);
  }

  /* Front */
  .card--front { top: 28px; background: var(--paper); }
  .card--front .edge-band {
    position: absolute; left: 0; right: 0; bottom: 0; height: 9px;
    background: linear-gradient(90deg, var(--ocean), var(--teal));
  }
  .card--front .ghost-disc {
    position: absolute; left: 110px; top: -40px;
    width: 330px; height: 330px; border-radius: 50%;
    background: var(--ghost);
  }
  .brand {
    position: absolute; left: 300px; top: 108px;
    display: flex; align-items: center; gap: 20px;
  }
  .brand__dot {
    width: 44px; height: 44px; border-radius: 50%;
    background: var(--teal);
  }
  .brand__name {
    font-family: "Montserrat", sans-serif;
    font-weight: 500; font-size: 30px; letter-spacing: 9px;
    color: var(--navy);
  }
  .divider {
    position: absolute; left: 226px; right: 40px; top: 206px;
    height: 1px; background: var(--rule);
  }
  .contact {
    position: absolute; left: 44px; top: 168px;
    font-family: "Arimo", sans-serif; color: var(--ink);
  }
  .contact__name {
    font-family: "Montserrat", sans-serif; font-weight: 600;
    font-size: 20px; color: var(--teal); text-transform: uppercase;
    letter-spacing: 0.5px;
  }
  .contact__role { font-size: 15px; margin-bottom: 12px; }
  .contact__list { list-style: none; font-size: 15px; line-height: 23px; }
  .contact__list li { display: flex; align-items: center; gap: 8px; }
  .contact__list svg { width: 16px; height: 16px; flex: none; }
  .contact__accent { color: var(--teal); }

  /* Back */
  .card--back {
    top: 447px;
    background: linear-gradient(135deg, var(--ocean) 0%, var(--teal) 55%, var(--ocean) 100%);
  }
  .card--back .ghost-disc {
    position: absolute; left: 130px; top: -30px;
    width: 340px; height: 340px; border-radius: 50%;
    background: rgba(20, 70, 90, 0.12);
  }
  .card--back .brand__name {
    position: absolute; left: 0; right: 0; top: 170px;
    text-align: center; font-size: 40px; letter-spacing: 12px;
    color: rgba(22, 50, 68, 0.85);
  }
</style>
</head>
<body>
  <section class="card card--front" aria-label="Card front">
    <div class="ghost-disc"></div>
    <div class="brand">
      <span class="brand__dot"></span>
      <span class="brand__name">TIDEMERE</span>
    </div>
    <div class="divider"></div>
    <div class="contact">
      <p class="contact__name">Daniel Hartley</p>
      <p class="contact__role">Managing Director</p>
      <ul class="contact__list">
        <li>
          <svg viewBox="0 0 16 16" fill="none" stroke="#4fbab3" stroke-width="1.4"><rect x="1" y="1" width="14" height="14" rx="2"/><path d="M5 4c-1 1-1 3 1 5s4 3 5 2l-1.5-1.5-1.3.7-2.2-2.2.7-1.3z"/></svg>
          044-987 650 321
        </li>
        <li>
          <svg viewBox="0 0 16 16" fill="none" stroke="#4fbab3" stroke-width="1.4"><rect x="1" y="3" width="14" height="10"/><path d="M1 3l7 6 7-6"/></svg>
          hello@tidemere.com
        </li>
        <li>
          <svg viewBox="0 0 16 16" fill="none" stroke="#4fbab3" stroke-width="1.3"><circle cx="8" cy="8" r="7"/><ellipse cx="8" cy="8" rx="3" ry="7"/><path d="M1 8h14M2.5 4.5h11M2.5 11.5h11"/></svg>
          <span>www.<span class="contact__accent">tidemere</span>.com</span>
        </li>
      </ul>
    </div>
    <div class="edge-band"></div>
  </section>

  <section class="card card--back" aria-label="Card back">
    <div class="ghost-disc"></div>
    <p class="brand__name">TIDEMERE</p>
  </section>
</body>
</html>
```